Corvane Electrical Solutions

On one side. LOGO (underneath:) Commercial Industrial Residential

- NAME & CONTACT DETAILS

Marcus T. Hollings
Project Manager

(Cell icon) (441) 582-6197
(Email icon) cvnelectricalsoultions@mailventra.com
(Facebook & Instagram icons )@cvnelectricalsolutions

Other side: LOGO - underneath ELECTRICAL CONSTRUCTION & MAINTENANCE . LED LIGHTING & AUTOMATION . LIFE SAFETY SYSTEMS (FIRE ALARM / SECURITY) . DATA & COMMUNICATION

```html
<!DOCTYPE html>
<html lang="en">
<head>
<meta charset="UTF-8">
<title>Corvane Electrical Solutions – Business Card</title>
<link href="https://fonts.googleapis.com/css2?family=Montserrat:wght@400;500;600&family=Roboto+Condensed:wght@700&display=swap" rel="stylesheet">
<style>
  :root {
    --backdrop: #2b2b2d;
    --card: #ffffff;
    --teal: #0f4f67;
    --band: #216678;
    --ink: #3a3a3a;
  }
  * { margin: 0; padding: 0; box-sizing: border-box; }
  html, body {
    width: 1200px; height: 1200px; overflow: hidden;
    background: var(--backdrop);
    font-family: "Montserrat", sans-serif;
  }
  .card {
    position: absolute; left: 286px;
    width: 612px; height: 368px;
    background: var(--card);
    overflow: hidden;
  }
  .card--front { top: 217px; }
  .card--back { top: 624px; }

  /* Front */
  .brand {
    position: absolute; top: 128px; left: 0; width: 100%;
    display: flex; justify-content: center; align-items: center; gap: 16px;
  }
  .brand__mark { width: 30px; height: 30px; background: var(--teal); }
  .brand__name {
    font-weight: 500; font-size: 21px; line-height: 1.12;
    letter-spacing: 2.4px; color: var(--teal); text-transform: uppercase;
  }
  .services {
    position: absolute; top: 309px; left: 60px; right: 60px;
    font-size: 11.2px; line-height: 17px; letter-spacing: 0.2px;
    color: var(--ink); text-transform: uppercase;
  }
  .services .dot { color: var(--teal); font-weight: 600; margin: 0 2px; }

  /* Back */
  .person {
    position: absolute; top: 162px; right: 319px; text-align: right;
  }
  .person__name {
    font-family: "Roboto Condensed", sans-serif; font-weight: 700;
    font-size: 20px; color: var(--teal); line-height: 1; letter-spacing: -0.2px;
  }
  .person__role { font-size: 11px; font-weight: 500; color: var(--ink); margin-top: 5px; }
  .divider {
    position: absolute; left: 306px; top: 153px;
    width: 1px; height: 55px; background: var(--teal);
  }
  .contacts {
    position: absolute; left: 318px; top: 154px; list-style: none;
    font-size: 11.2px; font-weight: 500; color: var(--ink);
  }
  .contacts li { display: flex; align-items: center; gap: 5px; height: 18.5px; }
  .contacts svg { width: 12px; height: 12px; flex: none; }
  .band {
    position: absolute; left: 0; bottom: 0; width: 100%; height: 20px;
    background: var(--band);
  }
</style>
</head>
<body>
  <section class="card card--front">
    <div class="brand">
      <span class="brand__mark"></span>
      <div class="brand__name">Corvane<br>Electrical<br>Solutions</div>
    </div>
    <p class="services">
      Electrical Construction &amp; Maintenance <span class="dot">•</span> LED Lighting &amp; Automation<br>
      <span class="dot">•</span> Life Safety Systems (Fire Alarm / Security) <span class="dot">•</span> Data &amp; Communication
    </p>
  </section>

  <section class="card card--back">
    <div class="person">
      <div class="person__name">MARCUS T. HOLLINGS</div>
      <div class="person__role">Project Manager</div>
    </div>
    <div class="divider"></div>
    <ul class="contacts">
      <li>
        <svg viewBox="0 0 12 12" aria-hidden="true"><circle cx="6" cy="6" r="5.4" fill="none" stroke="#0f4f67" stroke-width="0.9"/><path d="M4.2 3.4l1 1.1-.5.7c.4.8 1 1.4 1.8 1.8l.7-.5 1.1 1-.6.9C5.8 8.2 3.8 6.2 3.6 4z" fill="#0f4f67"/></svg>
        (441) 582-6197
      </li>
      <li>
        <svg viewBox="0 0 12 12" aria-hidden="true"><circle cx="6" cy="6" r="5.4" fill="none" stroke="#0f4f67" stroke-width="0.9"/><rect x="3.4" y="4.2" width="5.2" height="3.6" fill="none" stroke="#0f4f67" stroke-width="0.8"/><path d="M3.4 4.2L6 6.2l2.6-2" fill="none" stroke="#0f4f67" stroke-width="0.8"/></svg>
        cvnelectricalsoultions@mailventra.com
      </li>
      <li>
        <svg viewBox="0 0 12 12" aria-hidden="true"><circle cx="6" cy="6" r="5.4" fill="none" stroke="#0f4f67" stroke-width="0.9"/></svg>
        <svg viewBox="0 0 12 12" aria-hidden="true"><circle cx="6" cy="6" r="5.4" fill="none" stroke="#0f4f67" stroke-width="0.9"/></svg>
        @cvnelectricalsolutions
      </li>
    </ul>
    <div class="band"></div>
  </section>
</body>
</html>
```